web page design with coding

We are a start up insurance agency who needs to design a full functional web page. we recently did a postcard design though artmeadow I will upload the final project for you to see the color scheme/font we would like to continue to use. I also have a rough draft of verbage I would like our website to have. I will upload that as well.

Reason: I am sorry but the person who will make the final decision on the website is out of the country at the moment and will make the final decision when he returns.

Industry/Entity Type

Insurance

Coding

Coded - Design and coding required

```html
<!DOCTYPE html>
<html lang="en">
<head>
<meta charset="utf-8">
<title>Solidus Insurance Group</title>
<link href="https://fonts.googleapis.com/css2?family=Open+Sans:wght@400;600;700&display=swap" rel="stylesheet">
<style>
:root{
  --green:#2e8540;
  --navy:#1f3b6e;
  --ink:#333333;
  --muted:#555555;
  --dark:#3d3d3d;
  --darker:#2c2c2c;
  --light:#efefef;
  --white:#ffffff;
}
*{box-sizing:border-box;margin:0;padding:0}
html,body{width:1200px;height:2406px;overflow:hidden}
body{position:relative;font-family:"Open Sans",Arial,sans-serif;color:var(--ink);background:var(--white)}
.abs{position:absolute}

.top-rule{left:0;top:0;width:1200px;height:4px;background:var(--green)}
.header{left:0;top:4px;width:1200px;height:127px;background:var(--white)}
.brand{left:99px;top:40px;display:flex;align-items:center;gap:12px}
.brand-square{width:34px;height:34px;background:var(--navy)}
.brand-name{font-size:22px;font-weight:600;color:var(--navy);line-height:1.1}
.nav a{position:absolute;top:58px;font-size:12.5px;color:var(--ink);text-decoration:none}
.nav a.active{color:var(--green)}
.nav-underline{left:427px;top:126px;width:42px;height:3px;background:var(--green)}
.search-btn{left:1059px;top:51px;width:42px;height:33px;background:var(--green);border-radius:3px}

.hero{left:0;top:131px;width:1200px;height:450px;background:linear-gradient(100deg,#d6dadf 0%,#bfc6cd 40%,#9aa3ad 70%,#4d535b 100%)}
.hero-brand{left:99px;top:330px;font-size:30px;font-weight:600;color:var(--white)}
.hero-title{left:99px;top:412px;font-size:45px;font-weight:600;color:var(--white)}
.hero-arrow{top:344px;width:24px;height:24px}
.hero-shadow{left:200px;top:578px;width:800px;height:28px}

.about-title{left:99px;top:636px;font-size:26px;font-weight:600;color:var(--green)}
.about-text{left:99px;top:697px;width:568px;font-size:12.5px;line-height:30px;color:var(--muted);text-align:justify}
.btn{top:879px;height:43px;border-radius:3px;color:var(--white);font-size:15px;font-weight:600;display:flex;align-items:center;justify-content:center}
.btn-green{left:99px;width:167px;background:var(--green)}
.btn-navy{left:292px;width:165px;background:var(--navy)}
.about-photo{left:714px;top:670px;width:386px;height:225px;border:4px solid var(--white);box-shadow:0 0 4px rgba(0,0,0,.35);background:linear-gradient(90deg,#aeb8c4,#d9dde2 50%,#8995a3)}

.services{left:0;top:974px;width:1200px;height:566px;background:var(--dark)}
.services-title{left:0;top:1020px;width:1200px;text-align:center;font-size:26px;font-weight:600;color:var(--white)}
.services-intro{left:200px;top:1088px;width:800px;text-align:center;font-size:12.5px;line-height:27px;color:var(--white)}
.card{top:1238px;width:236px;height:250px;background:var(--white);box-shadow:0 2px 4px rgba(0,0,0,.3)}
.card-icon{position:absolute;left:62px;top:-56px;width:112px;height:112px;border-radius:50%;background:var(--white);border:3px solid var(--green)}
.card-title{position:absolute;top:86px;width:100%;text-align:center;font-size:16px;color:var(--ink)}
.card-text{position:absolute;top:128px;left:0;width:100%;text-align:center;font-size:11.5px;line-height:21px;color:var(--muted);white-space:nowrap}
.card-link{position:absolute;top:204px;width:100%;text-align:center;font-size:11.5px;color:var(--green)}

.types-rule{left:596px;top:1540px;width:8px;height:202px;background:var(--green)}
.type-title{top:1588px;font-size:24px;font-weight:600;color:var(--navy)}
.type-text{font-size:11.5px;line-height:29px;color:var(--muted);white-space:nowrap}
.type-link{top:1815px;font-size:12px;color:var(--green);text-decoration:underline}
.types-badge{left:460px;top:1742px;width:278px;height:127px;background:var(--green);border:3px solid var(--white);outline:3px solid var(--green);color:var(--white);text-align:center;display:flex;flex-direction:column;justify-content:center}
.types-badge .l1{font-size:29px;line-height:34px}
.types-badge .l2{font-size:41px;line-height:46px;font-weight:600}

.partners{left:0;top:1933px;width:1200px;height:152px;background:var(--light)}
.partner{top:1982px;height:54px;border-radius:6px;background:#cfd3d6}

.footer{left:0;top:2085px;width:1200px;height:249px;background:var(--dark);color:var(--white)}
.f-head{top:2124px;font-size:15px;font-weight:600;color:var(--white)}
.f-list{list-style:none;font-size:12px;line-height:27px;color:var(--white)}
.f-list li::before{content:"» ";}
.f-about{left:99px;top:2160px;width:200px;font-size:12px;line-height:26px;text-align:justify;color:var(--white)}
.f-more{left:99px;top:2268px;font-size:12px;color:var(--white)}
.f-contact{left:693px;top:2160px;font-size:12px;line-height:26px;color:var(--white)}
.social{top:2174px;width:36px;height:36px;border:2px solid var(--white);border-radius:50%}
.bottom-bar{left:0;top:2334px;width:1200px;height:72px;background:var(--darker)}
.copyright{left:0;top:2359px;width:1200px;text-align:center;font-size:12px;color:var(--white)}
</style>
</head>
<body>

<div class="abs top-rule"></div>
<header class="abs header"></header>
<div class="abs brand"><div class="brand-square"></div><div class="brand-name">Solidus<br>Insurance Group</div></div>
<nav class="nav">
  <a class="active" style="left:433px">Home</a>
  <a style="left:529px">About Us</a>
  <a style="left:645px">Products &amp; Services</a>
  <a style="left:820px">Insurance</a>
  <a style="left:940px">Contact Us</a>
</nav>
<div class="abs nav-underline"></div>
<div class="abs search-btn">
  <svg width="42" height="33" viewBox="0 0 42 33"><circle cx="20" cy="15" r="5" fill="none" stroke="#fff" stroke-width="2.2"/><line x1="24" y1="19" x2="27" y2="22" stroke="#fff" stroke-width="2.4"/></svg>
</div>

<div class="abs hero" role="img" aria-label="Photo of an insurance agent meeting a client at an office desk"></div>
<div class="abs hero-brand">Solidus Insurance Group</div>
<div class="abs hero-title">We work For You</div>
<svg class="abs hero-arrow" style="left:40px" viewBox="0 0 24 24"><polyline points="15,5 8,12 15,19" fill="none" stroke="#fff" stroke-width="2.5"/></svg>
<svg class="abs hero-arrow" style="left:1136px" viewBox="0 0 24 24"><polyline points="9,5 16,12 9,19" fill="none" stroke="#fff" stroke-width="2.5"/></svg>
<svg class="abs hero-shadow" viewBox="0 0 800 28"><defs><radialGradient id="sh" cx="50%" cy="0%" r="50%"><stop offset="0" stop-color="#000" stop-opacity=".22"/><stop offset="1" stop-color="#000" stop-opacity="0"/></radialGradient></defs><ellipse cx="400" cy="0" rx="400" ry="28" fill="url(#sh)"/></svg>

<h2 class="abs about-title">About Our Solidus Insurance Group</h2>
<p class="abs about-text">Established in 2015, Solidus Insurance Group is a full service independent insurance agency. Our licensed agents have the experience to custom tailor a program to meet your specific needs &amp; our professional support staff will provide you with top notch customer service to help ease the burden of managing your insurance program. We have established relationships with carriers in order to offer you the most competitive products and services available in the marketplace today.</p>
<div class="abs btn btn-green">Read More Info</div>
<div class="abs btn btn-navy">Contact Us Now</div>
<div class="abs about-photo" role="img" aria-label="Photo of a smiling businessman in a suit standing in an office"></div>

<section class="abs services"></section>
<h2 class="abs services-title">Our Products And Services</h2>
<p class="abs services-intro">Solidus Insurance Group is a one stop shop for all of your personal and business insurance needs. With our established relationships<br>and market knowledge, we will tailor an insurance program specifically designed to meet your needs.</p>

<div class="abs card" style="left:99px">
  <div class="card-icon"><svg width="106" height="106" viewBox="0 0 106 106"><rect x="36" y="40" width="34" height="16" rx="4" fill="#2e8540"/><path d="M42 40 L47 31 H60 L65 40Z" fill="#2e8540"/><path d="M30 66 Q53 78 76 66" fill="none" stroke="#2e8540" stroke-width="5"/></svg></div>
  <div class="card-title">Nam Omnis Harum</div>
  <div class="card-text">Cu nam omnis harum necessitati-<br>bus. Eu eam atomorum deterruiss<br>et, atqui vitae democritum</div>
  <div class="card-link">Read More Info &gt;&gt;</div>
</div>
<div class="abs card" style="left:354px">
  <div class="card-icon"><svg width="106" height="106" viewBox="0 0 106 106"><g transform="rotate(-18 50 48)"><rect x="30" y="44" width="40" height="16" rx="4" fill="#2e8540"/><path d="M37 44 L43 34 H58 L64 44Z" fill="#2e8540"/></g><line x1="30" y1="74" x2="80" y2="74" stroke="#2e8540" stroke-width="4"/><line x1="80" y1="52" x2="80" y2="74" stroke="#2e8540" stroke-width="4"/></svg></div>
  <div class="card-title">Graece nostro susci</div>
  <div class="card-text">Cu nam omnis harum necessitati-<br>bus. Eu eam atomorum deterruiss<br>et, atqui vitae democritum</div>
  <div class="card-link">Read More Info &gt;&gt;</div>
</div>
<div class="abs card" style="left:610px">
  <div class="card-icon"><svg width="106" height="106" viewBox="0 0 106 106"><path d="M27 52 Q53 18 79 52Z" fill="#2e8540"/><path d="M53 52 V74 Q53 80 47 78" fill="none" stroke="#2e8540" stroke-width="4"/></svg></div>
  <div class="card-title">Brute saperet ponder</div>
  <div class="card-text">Cu nam omnis harum necessitati-<br>bus. Eu eam atomorum deterruiss<br>et, atqui vitae democritum</div>
  <div class="card-link">Read More Info &gt;&gt;</div>
</div>
<div class="abs card" style="left:865px">
  <div class="card-icon"><svg width="106" height="106" viewBox="0 0 106 106"><path d="M25 52 L53 28 L81 52" fill="none" stroke="#2e8540" stroke-width="5"/><rect x="33" y="52" width="40" height="22" fill="none" stroke="#2e8540" stroke-width="5"/></svg></div>
  <div class="card-title">Nam Omnis Harum</div>
  <div class="card-text">Cu nam omnis harum necessitati-<br>bus. Eu eam atomorum deterruiss<br>et, atqui vitae democritum</div>
  <div class="card-link">Read More Info &gt;&gt;</div>
</div>

<div class="abs types-rule"></div>
<svg class="abs" style="left:99px;top:1572px" width="50" height="52" viewBox="0 0 50 52"><path d="M4 24 L25 4 L46 24 V30 L25 12 L4 30Z" fill="#1f3b6e"/><path d="M12 32 Q25 22 38 32 V48 H12Z" fill="#1f3b6e"/></svg>
<h3 class="abs type-title" style="left:168px">Business Insurance</h3>
<p class="abs type-text" style="left:99px;top:1651px">Cu nam omnis harum necessitatibus. Eu eam atomorum deterruisset, atqui vitae<br>democritum eu duo, has dico vitae in Cu nam omnis harum necessitatibus. Eu<br>eam atomorum deterruisset, atqui vitae democritum eu duo,<br>Legimus probatus tacimates eu has, cu vel utinam ubique<br>percipit, vis accumsan deseruisse eu</p>
<div class="abs type-link" style="left:99px">Click to View More Info &gt;&gt;</div>

<svg class="abs" style="left:653px;top:1570px" width="46" height="56" viewBox="0 0 46 56"><circle cx="14" cy="8" r="7" fill="#1f3b6e"/><rect x="4" y="17" width="20" height="37" rx="4" fill="#1f3b6e"/><path d="M22 24 L33 20 L44 24 V34 Q44 44 33 48 Q22 44 22 34Z" fill="#fff" stroke="#1f3b6e" stroke-width="3"/><path d="M28 34 L32 38 L39 29" fill="none" stroke="#1f3b6e" stroke-width="3"/></svg>
<h3 class="abs type-title" style="left:720px">Personal Insurance</h3>
<p class="abs type-text" style="left:653px;top:1651px">Cu nam omnis harum necessitatibus. Eu eam atomorum deterruisset, atqui vitae<br>democritum eu duo, has dico vitae in Cu nam omnis harum necessitatibus. Euhk</p>
<p class="abs type-text" style="left:762px;top:1709px">eam atomorum deterruisset, atqui vitae democritum atqui in<br>Legimus probatus tacimates eu has, cu vel utinam ubique<br>percipit, vis accumsan deseruisse eu</p>
<div class="abs type-link" style="left:762px">Click to View More Info &gt;&gt;</div>

<div class="abs types-badge"><div class="l1">Types Of</div><div class="l2">Insurance</div></div>

<section class="abs partners"></section>
<svg class="abs" style="left:58px;top:1996px" width="18" height="24" viewBox="0 0 18 24"><polyline points="14,3 5,12 14,21" fill="none" stroke="#bbb" stroke-width="3"/></svg>
<svg class="abs" style="left:1128px;top:1996px" width="18" height="24" viewBox="0 0 18 24"><polyline points="4,3 13,12 4,21" fill="none" stroke="#bbb" stroke-width="3"/></svg>
<div class="abs partner" style="left:136px;width:177px"></div>
<div class="abs partner" style="left:401px;width:184px"></div>
<div class="abs partner" style="left:666px;width:131px"></div>
<div class="abs partner" style="left:890px;width:188px"></div>

<footer class="abs footer"></footer>
<div class="abs f-head" style="left:99px">ABOUT</div>
<p class="abs f-about">Established in 2015, Solidus Insurance Group is a full service independent insurance agency. Our licensed agents notch</p>
<div class="abs f-more">[ Read More ]</div>
<div class="abs f-head" style="left:346px">MENUS</div>
<ul class="abs f-list" style="left:346px;top:2156px"><li>Home</li><li>About us</li><li>Our services</li><li>Blog</li><li>Contact us</li></ul>
<div class="abs f-head" style="left:492px">QUICK LINKS</div>
<ul class="abs f-list" style="left:492px;top:2156px"><li>Site map</li><li>Terms and Conditions</li><li>Disclaimer</li><li>Privacy Policy</li><li>Contact us</li></ul>
<div class="abs f-head" style="left:693px">CONTACT US</div>
<div class="abs f-contact">
  <svg width="14" height="12" viewBox="0 0 14 12" style="vertical-align:-1px"><path d="M1 6 L7 1 L13 6 H11 V11 H3 V6Z" fill="#fff"/></svg>&nbsp;&nbsp; 1280 Harbor Ave Suite 300<br>
  <span style="padding-left:26px">Miami, FL 33101</span><br>
  <div style="height:10px"></div>
  <svg width="10" height="14" viewBox="0 0 10 14" style="vertical-align:-2px"><rect x="1" y="0" width="8" height="14" rx="1.5" fill="#fff"/></svg>&nbsp;&nbsp;&nbsp; Call Us : (555)014-2290<br>
  <span style="padding-left:26px">(555)016-7731</span><br>
  <div style="height:8px"></div>
  <svg width="14" height="14" viewBox="0 0 14 14" style="vertical-align:-2px"><circle cx="7" cy="7" r="6" fill="#fff"/></svg>&nbsp;&nbsp; www.sig-cover.com
</div>
<div class="abs f-head" style="left:921px">CONNECT US WITH</div>
<div class="abs social" style="left:921px"></div>
<div class="abs social" style="left:967px"></div>
<div class="abs social" style="left:1013px"></div>
<div class="abs social" style="left:1059px"></div>

<div class="abs bottom-bar"></div>
<div class="abs copyright">© &nbsp;Companyname 2016 . All Rights Reserved</div>

</body>
</html>
```